Flyer Vacation Gift Certificate

I need to create a beautiful flyer 8.5 x 11 PDF format flyer design. <br/><br/>Instructions:<br/>The flyer will really be a gift voucher for a las vegas vacation getaway. So must have a Las Vegas Theme exciting fun<br/><br/>The voucher should have two modules that will be editable. <br/>Must have a "Compliments Of" area and also must have an "Exclusively For" area<br/><br/>Keep in mind that this flyer will be printed so keep that in mind :)<br/><br/>Here the is the content for the vacation voucher:<br/><br/>There is no doubt that Las Vegas is one of the hottest travel destinations around the world. In fact, some people would even go as far as<br/>saying that perhaps it is THE hottest place to visit. Enjoy up to 4 nights of resort/casino accommodations in exciting Las Vegas, NV. Millions of people travel to this exciting city each year to enjoy its thrills. Thanks to the business you received this certificate from, now you can enjoy exciting Las Vegas, NV too!<br/><br/>Features:<br/>*Travel 7 Days A Week<br/>*Stay Your Choice Of Nights (1-4 Nights)<br/>*Good For Two Adults & Two Children<br/>*Pay Just The Taxes & Fees<br/>*Multiple Travel Date Requests Allowed<br/>*Fully Transferable To Another Person<br/>*Just A 30 Days Advance Notice Required<br/>*You Will Have 12 Months To Complete Travel After Redemption<br/><br/>HOW CAN WE DO THIS?<br/><br/>We contract with the world leading hotel chains and resorts to help them fill their otherwise empty rooms.<br/><br/>We help fill empty rooms which the hotels, resorts and cruise lines turn into additional revenue from other areas of their property and future bookings.<br/><br/>Hotels rarely experience full occupancy, yet they remain open, providing rooms and services at fixed costs. So when hotels give out their rooms by partnering with marketing companies like us, they might miss out on the room fee, but they already didn't have that in the first place, at least now they have the opportunity to gain a customer for their in-house restaurants, room service, their casinos, an extra day stay, future bookings, etc.<br/><br/>VIEW ALL THE DETAILS OF THIS SPECIAL OFFER AND REDEEM ONLINE AT <br/>WWW.TOPAZVOUCHERDESK.COM<br/><br/>Certificate ID # 47261-38504<br/>Expires 02/29/2020<br/><br/><br/>*terms and conditions apply see website for details<br/><br/>KEEP IN MIND THE EXAMPLES I AM UPLOADING ARE SIMPLY TO SHOW YOU THAT THEY CONTAIN THE "COMPLIMENTS OF" AND "EXCLUSIVELY FOR" ELEMENTS. THESE MUST BE INCLUDED IN NEW DESIGN. PLEASE ONLY USE THE CONTENT I PROVIDED IN BRIEF, DONT USE CONTENT FROM EXAMPLES.

Target Market(s)

CONSUMERS THAT HAVE BEEN REWARDED WITH A VACATION CERTIFICATE FOR DOING BUSINESS WITH A COMPANY.

COMPANIES USE THESE AS MARKETING INCENTIVES TO ATTRACT MORE CUSTOMERS AND TO REWARD LOYALTY, ETC.

Industry/Entity Type

Travel Industry

Colors

Designer to choose colors to be used in the design.

Requirements
Must have
• I need to create a beautiful flyer 8.5 x 11 PDF format flyer design.
• Instructions:
• The flyer will really be a gift voucher for a las vegas vacation getaway. So must have a Las Vegas Theme exciting fun
• The voucher should have two modules that will be editable.
• Must have a "Compliments Of" area and also must have an "Exclusively For" area
• Keep in mind that this flyer will be printed so keep that in mind :)
• Here the is the content for the vacation voucher:
• There is no doubt that Las Vegas is one of the hottest travel destinations around the world. In fact, some people would even go as far as
• saying that perhaps it is THE hottest place to visit. Enjoy up to 4 nights of resort/casino accommodations in exciting Las Vegas, NV. Millions of people travel to this exciting city each year to enjoy its thrills. Thanks to the business you received this certificate from, now you can enjoy exciting Las Vegas, NV too!
• Features:
• *Travel 7 Days A Week
• *Stay Your Choice Of Nights (1-4 Nights)
• *Good For Two Adults & Two Children
• *Pay Just The Taxes & Fees
• *Multiple Travel Date Requests Allowed
• *Fully Transferable To Another Person
• *Just A 30 Days Advance Notice Required
• *You Will Have 12 Months To Complete Travel After Redemption
• HOW CAN WE DO THIS?
• We contract with the world leading hotel chains and resorts to help them fill their otherwise empty rooms.
• We help fill empty rooms which the hotels, resorts and cruise lines turn into additional revenue from other areas of their property and future bookings.
• Hotels rarely experience full occupancy, yet they remain open, providing rooms and services at fixed costs. So when hotels give out their rooms by partnering with marketing companies like us, they might miss out on the room fee, but they already didn't have that in the first place, at least now they have the opportunity to gain a customer for their in-house restaurants, room service, their casinos, an extra day stay, future bookings, etc.
• VIEW ALL THE DETAILS OF THIS SPECIAL OFFER AND REDEEM ONLINE AT
• WWW.TOPAZVOUCHERDESK.COM
• Certificate ID # 47261-38504
• Expires 02/29/2020
• *terms and conditions apply see website for details
• KEEP IN MIND THE EXAMPLES I AM UPLOADING ARE SIMPLY TO SHOW YOU THAT THEY CONTAIN THE "COMPLIMENTS OF" AND "EXCLUSIVELY FOR" ELEMENTS. THESE MUST BE INCLUDED IN NEW DESIGN. PLEASE ONLY USE THE CONTENT I PROVIDED IN BRIEF, DONT USE CONTENT FROM EXAMPLES.
Nice to have
• EXCITING LAS VEGAS IMAGES THAT MAKE SOMEONE WANT TO GO THERE

```html
<!DOCTYPE html>
<html lang="en">
<head>
<meta charset="utf-8">
<title>Las Vegas Vacation Gift Certificate</title>
<link href="https://fonts.googleapis.com/css2?family=Cormorant+SC:wght@500;600&family=Cinzel:wght@800&family=Josefin+Sans:wght@500;600&family=Oswald:wght@500&display=swap" rel="stylesheet">
<style>
  :root{
    --ink:#2b2b35;
    --ink-navy:#3d3f6b;
    --mint:#8fd0bc;
    --mint-soft:#abdcce;
    --teal:#65c7b1;
    --teal-deep:#6a9a8a;
    --forest:#4b6a5d;
    --ring:#1f2430;
    --lavender:#ecebf6;
    --paper:#ffffff;
  }
  html,body{margin:0;padding:0;overflow:hidden;background:var(--paper);}
  .flyer{
    position:relative;width:927px;height:1200px;overflow:hidden;
    background:var(--paper);color:var(--ink);
    font-family:"Cormorant SC",serif;font-weight:500;
  }
  .shapes{position:absolute;left:0;top:0;width:927px;height:1200px;}
  .intro{
    position:absolute;left:40px;top:62px;width:540px;margin:0;
    text-align:center;font-size:17px;line-height:20px;letter-spacing:1.3px;white-space:nowrap;
  }
  .intro-thanks{
    position:absolute;left:40px;top:204px;width:540px;margin:0;
    text-align:center;font-size:18px;line-height:22px;letter-spacing:1.1px;color:var(--ink-navy);white-space:nowrap;
  }
  .figure{font-family:"Josefin Sans",sans-serif;font-weight:600;}
  .compliments{
    position:absolute;left:629px;top:33px;width:298px;height:80px;
    background:var(--mint);border-radius:14px 0 0 14px;
  }
  .compliments-label{
    position:absolute;left:17px;top:6px;margin:0;white-space:nowrap;
    font-family:"Cinzel",serif;font-weight:800;font-size:27px;letter-spacing:.6px;color:var(--paper);
  }
  .sign-art{
    position:absolute;left:680px;top:126px;width:222px;height:280px;
    background:linear-gradient(180deg,#f8e3d2 0%,#fbefe6 60%,#f1f1f3 100%);
    border-radius:6px;
  }
  .features-title{
    position:absolute;left:550px;top:333px;margin:0;font-size:17px;letter-spacing:1px;font-weight:500;
  }
  .features{
    position:absolute;left:550px;top:393px;margin:0;padding:0;list-style:none;
    font-size:17px;line-height:27.4px;letter-spacing:1.1px;white-space:nowrap;
  }
  .features .wrap{padding-left:12px;}
  .certificate{
    position:absolute;right:20px;top:719px;margin:0;text-align:right;white-space:nowrap;
    font-size:17.5px;line-height:19.8px;letter-spacing:1.1px;
  }
  .redeem{
    position:absolute;left:567px;top:1057px;width:370px;margin:0;text-align:center;white-space:nowrap;
    font-size:16px;line-height:22px;letter-spacing:.9px;
  }
  .exclusive{
    position:absolute;left:521px;top:1132px;width:406px;height:59px;
    background:var(--forest);border-radius:14px 0 0 14px;
  }
  .exclusive-label{
    position:absolute;left:15px;top:10px;margin:0;white-space:nowrap;
    font-family:"Oswald",sans-serif;font-weight:500;font-size:27px;letter-spacing:-.5px;
    color:var(--paper);transform:scaleX(.82);transform-origin:left center;
  }
  .lettering-art{
    position:absolute;left:175px;top:990px;width:230px;height:190px;
    background:var(--lavender);border-radius:10px;opacity:.8;
  }
</style>
</head>
<body>
<main class="flyer">
  <svg class="shapes" viewBox="0 0 927 1200">
    <defs>
      <linearGradient id="cityNight" x1="0" y1="0" x2="0" y2="1">
        <stop offset="0" stop-color="#4d418c"/>
        <stop offset=".35" stop-color="#2c2748"/>
        <stop offset=".7" stop-color="#3b2a36"/>
        <stop offset="1" stop-color="#4a3035"/>
      </linearGradient>
      <linearGradient id="roadNight" x1="0" y1="0" x2="1" y2="1">
        <stop offset="0" stop-color="#3a2a3a"/>
        <stop offset="1" stop-color="#5a4040"/>
      </linearGradient>
    </defs>
    <circle class="corner-dot" cx="0" cy="104" r="63" fill="var(--mint-soft)"/>
    <circle class="corner-ring" cx="0" cy="104" r="83" fill="none" stroke="var(--ring)" stroke-width="3"/>
    <polygon role="img" aria-label="Las Vegas skyline and highway at dusk" points="66,265 507,561 507,802 286,951 66,1091" fill="url(#cityNight)"/>
    <polygon role="img" aria-label="Road with light trails and parked cars at night" points="507,802 736,951 507,1102" fill="url(#roadNight)"/>
    <polygon class="accent-triangle" points="286,409 507,264 507,561" fill="var(--teal-deep)"/>
    <polygon class="accent-triangle" points="286,951 507,802 507,1102" fill="var(--mint-soft)"/>
    <polygon class="hex-fill" points="812,956 840,906 896,906 924,956 896,1006 840,1006" fill="var(--teal)"/>
    <polygon class="hex-outline" points="753,956 782,906 839,906 868,956 839,1006 782,1006" fill="none" stroke="var(--ring)" stroke-width="3"/>
  </svg>

  <p class="intro">There is no doubt that Las Vegas is one of the<br>hottest travel destinations around the world.<br>In fact, some people would even go as far as saying<br>that perhaps it is THE hottest place to visit. Enjoy<br>up to <span class="figure">4</span> nights of resort/casino accommodations in<br>exciting Las Vegas, NV. Millions of people travel<br>to this exciting city each year to enjoy its thrills.</p>
  <p class="intro-thanks">Thanks to the business you<br>received this certificate from, now you can enjoy<br>exciting Las Vegas, NV too!</p>

  <section class="compliments"><p class="compliments-label">COMPLIMENTS OF</p></section>

  <div class="sign-art" role="img" aria-label="Illustrated Las Vegas Nevada welcome sign"></div>

  <p class="features-title">Features:</p>
  <ul class="features">
    <li>*Travel <span class="figure">7</span> Days A Week</li>
    <li>*Stay Your Choice Of Nights <span class="figure">(1-4</span> Nights)</li>
    <li>*Good For Two Adults &amp; Two Children</li>
    <li>*Pay Just The Taxes &amp; Fees</li>
    <li>*Multiple Travel Date Requests Allowed</li>
    <li>*Fully Transferable To Another Person</li>
    <li>*Just A <span class="figure">30</span> Days Advance Notice Required</li>
    <li>*You Will Have <span class="figure">12</span> Months To Complete</li>
    <li class="wrap">Travel After Redemption</li>
  </ul>

  <p class="certificate">Certificate ID # <span class="figure">47261-38504</span><br>Expires <span class="figure">02/29/2020</span><br>*terms and conditions apply<br>see website for details</p>

  <div class="lettering-art" role="img" aria-label="Faint hand-lettered Las Vegas decoration"></div>

  <p class="redeem">VIEW ALL THE DETAILS OF THIS SPECIAL<br>OFFER AND REDEEM ONLINE AT<br>WWW.TOPAZVOUCHERDESK.COM</p>

  <section class="exclusive"><p class="exclusive-label">EXCLUSIVELY FOR:</p></section>
</main>
</body>
</html>
```